DL Flyer Design

I need a DL flyer, double-sided designed for a Brisbane based outdoor group exercise/training company called Move Ahead! Move Ahead! provides group outdoor training, designed for the individual. It provides the support, motivation and one-on-one attention of personal training combined with the support of a group environment. The classes are fun, challenging and aim to develop confidence & fitness. Weight loss is not the focus, although it is a benefit.
Updates

Hi

I've just uploaded a high res version of the logo if you need.

Cheers
Tam

Target Market(s)

English speaking men & women aged 25 - 45, white-collar office jobs. Average-low level of fitness, not hugely 'fitness' oriented but want to improve quality of life, overall fitness, lose a bit of weight.

Computer and consumer literate. Live in suburban Brisbane, Australia.

Industry/Entity Type

Training

Requirements
Must have
• Double sided DL. Use of black, greens and white per attached photos. Use of 1300 572 914 (1300 RUN FAR) and website www.movaheadactive.com.au

Indicative copy and contents is posted in the comments section.

```html
<!DOCTYPE html>
<html lang="en">
<head>
<meta charset="utf-8">
<title>Move Ahead! – DL Flyer</title>
<link rel="stylesheet" href="https://fonts.googleapis.com/css2?family=Anton&family=Oswald:wght@400;600&family=Arimo:wght@400;700&display=swap">
<style>
  :root{
    --green:#6cbf2e;
    --green-deep:#4ea12a;
    --black:#141414;
    --grey:#c8c8c8;
    --grey-light:#e4e4e4;
    --white:#ffffff;
    --page:#ffffff;
  }
  *{box-sizing:border-box;margin:0;padding:0}
  html,body{width:1200px;height:900px;overflow:hidden;background:var(--page)}
  body{position:relative;font-family:"Arimo",Arial,sans-serif;color:var(--black)}

  .flyer{position:absolute;top:20px;width:424px;height:860px;background:var(--white);
    overflow:hidden;box-shadow:0 0 0 1px #ddd,0 3px 8px rgba(0,0,0,.15)}
  .flyer--front{left:160px}
  .flyer--back{left:610px}

  .swoosh{position:absolute;left:0;width:424px;pointer-events:none}
  .swoosh--top{top:0;height:130px}
  .swoosh--bottom{bottom:0;height:56px;z-index:3}

  .brand{position:absolute;top:40px;right:24px;display:flex;align-items:center;gap:10px;
    font-family:"Anton",Impact,sans-serif;font-size:52px;line-height:1;color:var(--green)}
  .brand__dot{width:16px;height:16px;border-radius:50%;background:var(--black)}

  .photo{position:absolute;z-index:2}
  .photo--front{left:302px;bottom:8px;width:120px;height:320px;
    background:linear-gradient(180deg,#e9d3a2 0%,#f2e06a 45%,#3a3a3a 100%);border-radius:60px 60px 0 0}
  .photo--back{left:272px;bottom:8px;width:150px;height:370px;
    background:linear-gradient(180deg,#d8b79c 0%,#7fc84a 45%,#5fae34 75%,#cfd3d4 100%);border-radius:70px 70px 0 0}

  .intro{position:absolute;left:48px;top:200px;width:320px;font-family:"Anton",Impact,sans-serif;font-size:20px;line-height:1.3;text-align:center}
  .intro__lead{display:block}
  .tagline{position:absolute;left:0;width:424px;top:262px;text-align:center;font-family:"Oswald",sans-serif;font-size:28px;color:var(--green);letter-spacing:.3px}
  .copy{position:absolute;left:36px;width:330px;font-size:14.5px;line-height:1.3}
  .copy strong.brand-word{color:var(--green)}
  .copy--one{top:318px}
  .copy--two{top:418px}
  .copy--three{top:468px;width:255px}
  .note{position:absolute;left:36px;top:530px;font-size:13px;color:var(--green)}
  .hook{position:absolute;left:36px;top:560px;font-family:"Anton",Impact,sans-serif;font-size:24px;line-height:1.2}
  .hook__cta{display:block;color:var(--green);font-size:46px;line-height:1.1}
  .call{position:absolute;left:36px;top:714px;font-family:"Anton",Impact,sans-serif;font-size:16px;line-height:1.25}
  .call__number{display:block;color:var(--green)}
  .call__web{display:block;font-family:"Arimo",sans-serif;font-weight:700;font-size:12px;margin-top:4px}

  .program{position:absolute;left:22px;top:250px;width:386px}
  .program__title{font-family:"Anton",Impact,sans-serif;font-size:17px;margin-bottom:6px}
  .schedule{width:100%;border-collapse:separate;border-spacing:2px;table-layout:fixed;font-size:8.5px;text-align:center}
  .schedule th{background:var(--green);color:var(--white);font-weight:700;height:18px}
  .schedule td{background:var(--grey);height:30px;padding:1px}
  .schedule td.is-time{font-weight:700}
  .schedule td.is-tall{height:42px}
  .program__note{font-size:9px;margin-top:10px}

  .contact{position:absolute;left:22px;top:548px}
  .contact__label{font-family:"Anton",Impact,sans-serif;font-size:27px;line-height:1.2}
  .contact__number{font-family:"Anton",Impact,sans-serif;font-size:38px;color:var(--green);line-height:1.1}
  .contact__web{font-weight:700;font-size:14px;color:var(--green-deep);margin-top:6px}
  .contact__note{font-size:8px;margin-top:3px}
</style>
</head>
<body>

<section class="flyer flyer--front">
  <svg class="swoosh swoosh--top" viewBox="0 0 424 130" preserveAspectRatio="none">
    <path d="M0 0H210C140 20 60 50 0 110Z" fill="var(--grey-light)"/>
    <path d="M0 0H150C95 18 40 42 0 78Z" fill="var(--green)"/>
    <path d="M0 0H90C55 12 22 28 0 48Z" fill="var(--black)"/>
  </svg>
  <div class="brand"><span class="brand__dot"></span>Move Ahead!</div>

  <p class="intro"><span class="intro__lead">It's time to Move Ahead!</span>with group outdoor training,</p>
  <p class="tagline">Designed Just For You!</p>
  <p class="copy copy--one"><strong class="brand-word">Move Ahead!</strong> provides the unique combination of the one-on-one attention of personal training with the motivation and support of a group environment.</p>
  <p class="copy copy--two">Best of all, it's designed to fit fitness into your life - at an affordable price.</p>
  <p class="copy copy--three">Curious? Give it a shot with a 1 week <strong>free trial!</strong></p>
  <p class="note">(Guaranteed no hard sell at the end)</p>
  <p class="hook">tired of hanging about?<br>....Just<span class="hook__cta">Move Ahead!</span></p>
  <p class="call">Call Now :<span class="call__number">1300 572 914 (1300 RUN FAR)</span><span class="call__web">www.movaheadactive.com.au</span></p>

  <div class="photo photo--front" role="img" aria-label="Photo of a smiling woman in a yellow training top, hand on hip"></div>

  <svg class="swoosh swoosh--bottom" viewBox="0 0 424 80" preserveAspectRatio="none">
    <path d="M0 60C120 40 280 40 424 10V80H0Z" fill="var(--green)"/>
    <path d="M0 72C130 56 290 52 424 34V80H0Z" fill="var(--black)"/>
  </svg>
</section>

<section class="flyer flyer--back">
  <svg class="swoosh swoosh--top" viewBox="0 0 424 130" preserveAspectRatio="none">
    <path d="M0 0H210C140 20 60 50 0 110Z" fill="var(--grey-light)"/>
    <path d="M0 0H150C95 18 40 42 0 78Z" fill="var(--green)"/>
    <path d="M0 0H90C55 12 22 28 0 48Z" fill="var(--black)"/>
  </svg>
  <div class="brand"><span class="brand__dot"></span>Move Ahead!</div>

  <div class="program">
    <h2 class="program__title">Session Program:</h2>
    <table class="schedule">
      <thead>
        <tr><th>Time</th><th>Monday</th><th>Tuesday</th><th>Wednesday</th><th>Thursday</th><th>Friday</th><th>Saturday</th></tr>
      </thead>
      <tbody>
        <tr><td class="is-time">6.00 am</td><td>Cardio</td><td></td><td>Street boxing circuit</td><td>Cardio</td><td>Street boxing circuit</td><td>Work up</td></tr>
        <tr><td></td><td></td><td></td><td></td><td></td><td></td><td>One on One Sessions</td></tr>
        <tr><td class="is-time is-tall">6.00 pm</td><td>Strength</td><td>Cardio</td><td>Strength</td><td>Street boxing circuit</td><td></td><td></td></tr>
      </tbody>
    </table>
    <p class="program__note">Location: (**details not confirmed)</p>
  </div>

  <div class="contact">
    <p class="contact__label">Call Now :</p>
    <p class="contact__number">1300 572 914<br>(1300 RUN FAR)</p>
    <p class="contact__web">www.movaheadactive.com.au</p>
    <p class="contact__note">Location: (**details not confirmed)</p>
  </div>

  <div class="photo photo--back" role="img" aria-label="Photo of a smiling woman in green workout gear holding an exercise ball"></div>

  <svg class="swoosh swoosh--bottom" viewBox="0 0 424 80" preserveAspectRatio="none">
    <path d="M0 60C120 40 280 40 424 10V80H0Z" fill="var(--green)"/>
    <path d="M0 72C130 56 290 52 424 34V80H0Z" fill="var(--black)"/>
  </svg>
</section>

</body>
</html>
```